Business card design needed

We are a manufacturing business based in Archerfield, Brisbane, Queensland. We Insulate airconditioning ductwork and also manufacture some duct.
Updates

Hi guys, thanks for all the responses, they are looking really great

I have attached a couple of better quality photos of the products we use or manufacture, they don't "need" to be used in the card but i thought it was worth uploading them

I will be picking the final card in the next couple of days

Thanks for the response.

I think this will be the last update but i have included what we do so it can be added to the back of a card.

Target Market(s)

Local contractors

Industry/Entity Type

Business

Contact Information for Business Card

Korrin Insulation
Mark Delaney
87 Tullamore Road
Tarrabeen, QLD, 4175
mark@korrininsulation.example.com.au
Phone: 07 3914 2260

Requirements
Must have
• our logo which i have attached

Also, on the back of the card it would be nice to have what we do

-Duct lagging (internal and external)
-Manufacture of Z7 boxes
-Supply of glasswool, foam insulation, ductboard, foils, tapes & pins.

```html
<!DOCTYPE html>
<html lang="en">
<head>
<meta charset="utf-8">
<title>Korrin Insulation – Business Cards</title>
<link rel="stylesheet" href="https://fonts.googleapis.com/css2?family=Source+Sans+3:wght@400;600;700&display=swap">
<style>
  :root {
    --backdrop: #1f1f22;
    --card-white: #ffffff;
    --ink: #3a3a3c;
    --strip-grey: #5b5b5e;
    --orange-top: #e9592a;
    --orange-bottom: #f38b2b;
    --orange: #ee6f28;
    --tint: #fbeee6;
    --font: "Source Sans 3", sans-serif;
  }
  * { box-sizing: border-box; margin: 0; padding: 0; }
  html, body {
    width: 1200px; height: 743px; overflow: hidden;
    background: var(--backdrop);
    font-family: var(--font);
  }
  .sheet { position: relative; width: 1200px; height: 743px; }

  .card {
    position: absolute;
    width: 521px; height: 297px;
    border-radius: 22px;
    background: var(--card-white);
    box-shadow: 0 3px 10px rgba(0,0,0,.55);
    overflow: hidden;
  }
  .card--front   { left: 65px;  top: 50px; }
  .card--logo    { left: 630px; top: 55px; }
  .card--pattern { left: 65px;  top: 392px; }
  .card--orange  { left: 635px; top: 394px;
    background: linear-gradient(180deg, var(--orange-top), var(--orange-bottom)); }

  /* Brand name stand-in */
  .brand {
    position: absolute;
    display: flex; align-items: center; gap: 12px;
    color: var(--ink);
    font-weight: 700;
    white-space: nowrap;
  }
  .brand__square { background: var(--orange); flex: none; }
  .brand--light { color: #ffffff; }
  .brand--light .brand__square { background: #ffffff; }

  .card--front .brand { left: 26px; top: 118px; font-size: 25px; gap: 8px; }
  .card--front .brand__square { width: 22px; height: 22px; }

  .card--logo .brand,
  .card--orange .brand { left: 0; right: 0; top: 82px; justify-content: center; font-size: 42px; }
  .card--logo .brand__square,
  .card--orange .brand__square { width: 36px; height: 36px; }

  .card--pattern .brand { left: 0; right: 0; top: 112px; justify-content: center; font-size: 42px; }

  /* Front contact block */
  .web-strip {
    position: absolute; left: 295px; top: 44px;
    width: 22px; height: 210px;
    background: var(--strip-grey);
    display: flex; align-items: center; justify-content: center;
  }
  .web-strip span {
    transform: rotate(-90deg);
    color: #fff; font-size: 11px; letter-spacing: .3px; white-space: nowrap;
  }
  .contact-panel {
    position: absolute; left: 319px; top: 43px;
    width: 202px; height: 212px;
    background: linear-gradient(180deg, var(--orange-top), var(--orange-bottom));
    color: #fff;
    padding: 34px 0 0 9px;
  }
  .contact-panel__name { font-size: 19px; font-weight: 700; margin-bottom: 18px; }
  .contact-line { display: flex; gap: 5px; font-size: 13px; line-height: 17px; margin-bottom: 6px; }
  .contact-line svg { flex: none; margin-top: 4px; }
  .contact-line--email { font-size: 10px; }
  .contact-line--address { margin-top: 14px; }

  .web {
    position: absolute; left: 0; right: 0;
    text-align: center;
    font-size: 19px; letter-spacing: 2.4px;
    color: var(--ink);
  }
  .card--logo .web { top: 257px; }
  .card--pattern .web { top: 257px; }
  .card--orange .web { top: 258px; color: #fff; }

  .pattern-field {
    position: absolute; inset: 0;
    background: linear-gradient(160deg, var(--tint), #ffffff 70%);
  }
</style>
</head>
<body>
<main class="sheet">

  <section class="card card--front">
    <div class="brand"><span class="brand__square"></span>Korrin Insulation</div>
    <div class="web-strip"><span>www.korrininsulation.example.com</span></div>
    <div class="contact-panel">
      <p class="contact-panel__name">Mark Delaney</p>
      <p class="contact-line">
        <svg width="9" height="9" viewBox="0 0 10 10"><path d="M2 1l2 2-1 1.5a6 6 0 0 0 2.5 2.5L7 6l2 2-1.5 1.5C4 9 1 6 .5 2.5z" fill="#fff"/></svg>
        07 3914 2260
      </p>
      <p class="contact-line contact-line--email">
        <svg width="9" height="7" viewBox="0 0 10 8"><rect x=".5" y=".5" width="9" height="7" fill="none" stroke="#fff"/><path d="M.5 .5l4.5 4 4.5-4" fill="none" stroke="#fff"/></svg>
        mark@korrininsulation.example.com.au
      </p>
      <p class="contact-line contact-line--address">
        <svg width="9" height="11" viewBox="0 0 10 12"><path d="M5 0a4 4 0 0 1 4 4c0 3-4 8-4 8S1 7 1 4a4 4 0 0 1 4-4z" fill="#fff"/><circle cx="5" cy="4" r="1.5" fill="#ee6f28"/></svg>
        <span>87 Tullamore Road<br>Tarrabeen, QLD, 4175</span>
      </p>
    </div>
  </section>

  <section class="card card--logo">
    <div class="brand"><span class="brand__square"></span>Korrin Insulation</div>
    <p class="web">www.korrininsulation.example.com</p>
  </section>

  <section class="card card--pattern">
    <div class="pattern-field" role="img" aria-label="Faint repeating brand-square pattern in pale orange"></div>
    <div class="brand">Korrin Insulation</div>
    <p class="web">www.korrininsulation.example.com</p>
  </section>

  <section class="card card--orange">
    <div class="brand brand--light"><span class="brand__square"></span>Korrin Insulation</div>
    <p class="web">www.korrininsulation.example.com</p>
  </section>

</main>
</body>
</html>
```